Winery Section 199

We need a flyer design for our Accounting Firm that details the benefits of Internal Revenue Code Section 199. This will be marketed to Wineries and Vineyard Farmers We would like to see designs that are bold and utilize our logo and vineyard/winery type symbols colors.

SEE NEW COPY

Target Market(s)

US based wineries and vineyards, Targeting the owners of these companies

Industry/Entity Type

Accounting

Font styles to use
Decorative

Requirements
Must have
• one page - would like to be able to embed into email if possible.
I attached a bunch of logo files only because I don't know which type you need
Nice to have
• see the wording I attached, this is what I would like it to say in general - ok for you to edit if you like. (file 5)

```html
<!DOCTYPE html>
<html lang="en">
<head>
<meta charset="utf-8">
<title>Harlow, Pike &amp; Wren – Domestic Production Activities Deduction</title>
<link rel="stylesheet" href="https://fonts.googleapis.com/css2?family=Tinos:wght@400;700&display=swap">
<style>
  :root {
    --sky-glow: #fff3b0;
    --sky-gold: #f9c73c;
    --sky-amber: #ec9426;
    --hill-rust: #8a4424;
    --vine-row: #4e3a22;
    --vine-green: #3f4a24;
    --soil-dark: #2a2416;
    --ornament-cream: rgba(238, 236, 176, 0.62);
    --ornament-olive: rgba(168, 170, 84, 0.5);
    --ornament-plum: rgba(150, 70, 90, 0.25);
    --brand-navy: #1d3466;
    --panel-fill: rgba(226, 222, 220, 0.76);
    --ink: #161616;
  }
  * { margin: 0; padding: 0; box-sizing: border-box; }
  html, body { width: 1200px; height: 800px; overflow: hidden; }
  body { font-family: "Tinos", "Times New Roman", serif; color: var(--ink); }

  .flyer { position: relative; width: 1200px; height: 800px; overflow: hidden; }

  .vineyard-scene {
    position: absolute; inset: 0;
    background:
      radial-gradient(ellipse 45% 30% at 30% 24%, var(--sky-glow) 0%, var(--sky-gold) 40%, transparent 80%),
      linear-gradient(180deg, var(--sky-gold) 0%, var(--sky-amber) 24%, var(--hill-rust) 40%, var(--vine-row) 58%, var(--vine-green) 78%, var(--soil-dark) 100%);
  }

  .vine-ornament {
    position: absolute; top: 0; height: 800px;
    background:
      radial-gradient(ellipse 40% 12% at 50% 30%, var(--ornament-plum), transparent 70%),
      radial-gradient(ellipse 40% 12% at 50% 72%, var(--ornament-plum), transparent 70%),
      linear-gradient(180deg, var(--ornament-cream) 0%, var(--ornament-olive) 45%, var(--ornament-cream) 100%);
  }
  .vine-ornament--left {
    left: 0; width: 270px;
    -webkit-mask-image: linear-gradient(90deg, #000 0%, #000 60%, transparent 100%);
            mask-image: linear-gradient(90deg, #000 0%, #000 60%, transparent 100%);
  }
  .vine-ornament--right {
    right: 0; width: 270px;
    -webkit-mask-image: linear-gradient(270deg, #000 0%, #000 60%, transparent 100%);
            mask-image: linear-gradient(270deg, #000 0%, #000 60%, transparent 100%);
  }

  .brand {
    position: absolute; top: 32px; left: 0; width: 1200px;
    text-align: center; color: var(--brand-navy); font-weight: 700;
  }
  .brand__name { font-size: 49px; line-height: 1; letter-spacing: 0.5px; }
  .brand__tagline { margin-top: 7px; font-size: 20px; letter-spacing: 1.6px; text-transform: uppercase; }

  .message-panel {
    position: absolute; left: 251px; top: 153px; width: 699px; height: 617px;
    background: var(--panel-fill);
    box-shadow: 0 2px 12px rgba(0, 0, 0, 0.4);
    padding: 22px 26px 0;
    text-align: center; font-size: 21.5px; line-height: 29px;
    hyphens: auto; -webkit-hyphens: auto;
  }
  .message-panel p + p { margin-top: 18px; }
  .message-panel .contact { margin-top: 22px; hyphens: none; -webkit-hyphens: none; }
</style>
</head>
<body>
<main class="flyer">
  <div class="vineyard-scene" role="img" aria-label="Photograph of vineyard rows at sunset under a golden sky, filling the whole flyer"></div>
  <div class="vine-ornament vine-ornament--left" role="img" aria-label="Decorative grapevine scrollwork with grape clusters and leaves along the left edge"></div>
  <div class="vine-ornament vine-ornament--right" role="img" aria-label="Decorative grapevine scrollwork with grape clusters and leaves along the right edge"></div>

  <header class="brand">
    <div class="brand__name">Harlow, Pike &amp; Wren</div>
    <div class="brand__tagline">Certified Public Accountants, Inc</div>
  </header>

  <section class="message-panel">
    <p>Have you made the decision to keep jobs in the US by hiring here in the United States?</p>
    <p>Are you seeing profits as a result of this decision and other smart moves you’ve made while pursuing your passion in the Winemaking and Vineyard field?</p>
    <p>You should be taking advantage of the 9% Domestic Production Activities Deduction the IRS has offered available only to Profitable Wineries and Farmers located in the US paying wages in the US!</p>
    <p>You do not have to spend any additional funds of your hard earned profits to take advantage of this incredible deduction! Keep more money to grow your business or your retirement account.</p>
    <p>We would love to meet with you and explain how your profitable company can pay less taxes, and claim refunds from previous years with this outstanding deduction.</p>
    <p class="contact">Call Marlene Ostrow at 530-555-0148<br>mostrow@harlowpike.net</p>
  </section>
</main>
</body>
</html>
```